DOVR Business Card Design Project

Company Name: DOVR (Dove Operational Versatile Resources) JLT.
Office Address: Office No 218, Saffron Crest Tower, Palmera Bay Towers, Dubai, U.A.E
Company line of business:
1) Currently we have a POS solution for retail outlets like duty free shops, supermarkets, department stores etc... The solution is deployed in Harbor Gate Retail on 350 POS and in Coralline Port Retail on 100 POS. So our main line of business is the deployment of this solution in retail outlets locally or regionally. We have already deployed the solution in India and Australia.
2) Integration of other third party POS systems with an online credit authorization netwotk in the UAE. This will enable POS applications to connect directly to the acquiring banks without needing an EFT terminal like Paxoline or Tramodex. The credit card payment is completed at the POS.
3) Other solutions that are targeting retail outlets like mobile POS, queue busting solutions, stock taking solutions using hand held devices, transaction capture systems, etc...
4) Other IT services like support of call center solutions from Bramwell Systems and development of new solutions as per customer requirements.
We need a business card design for the company. We don't have any specific requirements and will eave up to the designers to come up with creative designs. At the moment we still don't have a letter head design and the only thing that we have is the company logo that we will upload shortly.
Updates
Dear All,
I just uploaded the logo source files. I am sorry for the delay.
Regards
Tarek Demirci
I would like the business cards to have the following details:
Company Tel No
Company Fax No
Company Website Address
Employee Name
Employee Title
Employee Mobile Number
Employee Email Address

```html
<!DOCTYPE html>
<html lang="en">
<head>
<meta charset="utf-8">
<title>DOVR Business Card</title>
<link rel="stylesheet" href="https://fonts.googleapis.com/css2?family=Questrial&family=Didact+Gothic&display=swap">
<style>
  :root {
    --page: #ffffff;
    --card: #000000;
    --ink: #ffffff;
    --accent: #1e8fd6;
    --band: #ffffff;
    --band-ink: #111111;
  }
  * { margin: 0; padding: 0; box-sizing: border-box; }
  html, body { width: 1200px; height: 900px; overflow: hidden; background: var(--page); }
  .canvas { position: relative; width: 1200px; height: 900px; }

  .card {
    position: absolute;
    width: 624px;
    height: 397px;
    background: var(--card);
    border-radius: 16px;
    overflow: hidden;
    box-shadow: 0 4px 8px rgba(0,0,0,0.35);
  }
  .card--front { left: 111px; top: 44px; }
  .card--back  { left: 449px; top: 460px; }

  .brand { position: absolute; display: flex; align-items: center; }
  .brand__dot { border-radius: 50%; background: var(--accent); flex: none; }
  .brand__name {
    font-family: "Questrial", sans-serif;
    color: var(--ink);
    line-height: 1;
    letter-spacing: 0.02em;
  }
  .card--front .brand { left: 50px; top: 140px; }
  .card--front .brand__dot { width: 110px; height: 110px; margin-right: 90px; }
  .card--front .brand__name { font-size: 100px; }

  .card--back .brand { left: 30px; top: 150px; }
  .card--back .brand__dot { width: 60px; height: 60px; margin-right: 62px; }
  .card--back .brand__name { font-size: 54px; }

  .person { position: absolute; left: 343px; top: 108px; color: var(--ink); font-family: "Questrial", sans-serif; }
  .person__name { font-size: 16px; font-weight: 700; line-height: 1.05; -webkit-text-stroke: 0.4px var(--ink); }
  .person__title { font-size: 14px; line-height: 1.1; -webkit-text-stroke: 0.4px var(--ink); }

  .contacts { position: absolute; left: 342px; top: 160px; list-style: none; font-family: "Didact Gothic", sans-serif; color: var(--ink); }
  .contacts li { position: absolute; left: 0; display: flex; align-items: center; white-space: nowrap; }
  .contacts svg { width: 16px; height: 16px; fill: var(--accent); margin-right: 19px; }
  .contacts .small { font-size: 10px; }
  .contacts .large { font-size: 12px; }

  .web-band {
    position: absolute; left: 0; top: 348px; width: 100%; height: 32px;
    background: var(--band); color: var(--band-ink);
    font-family: "Questrial", sans-serif; font-weight: 700; font-size: 18px;
    letter-spacing: 0.5em; text-align: center; line-height: 32px;
    -webkit-text-stroke: 0.5px var(--band-ink);
    padding-left: 0.5em;
  }
</style>
</head>
<body>
<main class="canvas">

  <section class="card card--front" aria-label="Card front">
    <div class="brand">
      <span class="brand__dot"></span>
      <span class="brand__name">DOVR</span>
    </div>
  </section>

  <section class="card card--back" aria-label="Card back">
    <div class="brand">
      <span class="brand__dot"></span>
      <span class="brand__name">DOVR</span>
    </div>

    <div class="person">
      <p class="person__name">John Smith</p>
      <p class="person__title">Director</p>
    </div>

    <ul class="contacts">
      <li style="top:2px">
        <svg viewBox="0 0 16 16" aria-hidden="true"><path d="M1 5c0-2 3-3 7-3s7 1 7 3v1h-3V5H4v1H1z"/><path d="M3 8l2-2h6l2 2v6H3z"/></svg>
        <span class="small">xxx-xxxxx</span>
      </li>
      <li style="top:32px">
        <svg viewBox="0 0 16 16" aria-hidden="true"><path d="M4 1h8v4H4z"/><path d="M1 6h14v7H1z"/><path d="M4 10h8v5H4z" fill="#000"/><path d="M5 11h6v4H5z"/></svg>
        <span class="small">xxx-xxxxx</span>
      </li>
      <li style="top:59px">
        <svg viewBox="0 0 16 16" aria-hidden="true"><path d="M8 1a7 7 0 100 14A7 7 0 008 1zm0 1.3c.9 0 1.9 2 2.1 5H5.9C6.1 4.3 7.1 2.3 8 2.3zM2.4 7.3c.2-2 1.4-3.7 3.2-4.5-.6 1.1-1 2.7-1.1 4.5zm0 1.4h2.1c.1 1.8.5 3.4 1.1 4.5-1.8-.8-3-2.5-3.2-4.5zM8 13.7c-.9 0-1.9-2-2.1-5h4.2c-.2 3-1.2 5-2.1 5zm2.4-.5c.6-1.1 1-2.7 1.1-4.5h2.1c-.2 2-1.4 3.7-3.2 4.5zm1.1-5.9c-.1-1.8-.5-3.4-1.1-4.5 1.8.8 3 2.5 3.2 4.5z"/></svg>
        <span class="large">www.dovr.com.au</span>
      </li>
      <li style="top:84px">
        <svg viewBox="0 0 16 16" aria-hidden="true"><path d="M5 1h6a1 1 0 011 1v12a1 1 0 01-1 1H5a1 1 0 01-1-1V2a1 1 0 011-1zm1 2v6h4V3z"/></svg>
        <span class="small">xxx-xxxxx</span>
      </li>
      <li style="top:104px">
        <svg viewBox="0 0 16 16" aria-hidden="true"><path d="M1 4h14v9H1z"/><path d="M1.5 4.5L8 9l6.5-4.5" fill="none" stroke="#000" stroke-width="1.2"/></svg>
        <span class="large">myemail@dovr.com</span>
      </li>
    </ul>

    <p class="web-band">www.dovr.com.au</p>
  </section>

</main>
</body>
</html>
```